NZ First of it's kind solutions directory and marketplace for busy Mums needs a business card design

We need a business card design for our new nationwide business in NZ (long term plans to go global). We provide solutions to the everyday challenges that busy Mums face by connecting them with quality communities and suppliers of carefully selected, relevant products and services. We sell direct via our online marketplace. The final design should communicate our values of inclusivity, quality and smart solutions. Colours should incorporate our logo colour palette of #477077 and #6ba8b2. Our website is at https://www.brightnestly.com

Target Market(s)

busy Mums, Age 28 – 50, female, income over $100K, location main centres NZ primarily but NZ wide. Is likely juggling work or career with a young family. Probably had hobbies which have fallen by the wayside.
-Wants to succeed in her chosen career without compromising on family life
-to successfully juggle her career without feeling like she is compromising her children
- Is time poor, something always has to give and it’s generally her health (she’ll stay up late, get stressed)
- probably ex corporate or professional career. Has discretional income

Industry/Entity Type

Business

Contact Information for Business Card

Lena Hartwell, Founder, BrightNestly.com (Strapline Click; Connect; Done), 48 Kowhai Terrace, Ferndale, Auckland 1071, New Zealand. Mob: 021 437 518 Ph: +64 (0)9 581 4706

Font styles to use
Other font styles liked:
• Raleway, and/or Architects Daughter

Colors
00a990
33b8a4
86cfc6
cfeae6

Requirements
Must have
• the above details, streamline. the logo and colours associated with those logos
Should not have
• foil or metallic colours

```html
<!DOCTYPE html>
<html lang="en">
<head>
<meta charset="utf-8">
<title>BrightNestly business card</title>
<link rel="stylesheet" href="https://fonts.googleapis.com/css2?family=Raleway:wght@800&family=Roboto:wght@400;500&display=swap">
<style>
  :root {
    --teal-dark: #477077;
    --teal-light: #6ba8b2;
    --paper: #ffffff;
    --backdrop: #e9ecec;
    --ink: #477077;
    --ink-soft: #5d8389;
  }
  * { box-sizing: border-box; margin: 0; padding: 0; }
  html, body { width: 1200px; height: 930px; overflow: hidden; }
  body {
    background: var(--backdrop);
    font-family: "Roboto", Arial, sans-serif;
    position: relative;
  }
  .card {
    position: absolute;
    left: 280px;
    width: 640px;
    height: 366px;
    border-radius: 18px;
    overflow: hidden;
    box-shadow: 0 6px 18px rgba(0,0,0,0.12);
  }
  /* Back of card */
  .card-back { top: 80px; background: var(--teal-dark); }
  .brand {
    position: absolute;
    left: 0; right: 0; top: 140px;
    display: flex; align-items: center; justify-content: center; gap: 18px;
  }
  .brand-dot {
    width: 54px; height: 54px; border-radius: 50%;
    background: var(--paper);
  }
  .brand-name {
    font-family: "Raleway", Arial, sans-serif;
    font-weight: 800;
    font-size: 62px;
    letter-spacing: -1px;
    color: var(--paper);
  }
  .back-url {
    position: absolute; left: 0; right: 0; bottom: 40px;
    text-align: center; color: var(--paper);
    font-size: 15px; letter-spacing: 0.6px;
  }
  /* Front of card */
  .card-front { top: 484px; background: var(--paper); }
  .front-wave { position: absolute; left: 0; top: 0; width: 640px; height: 366px; }
  .front-mark {
    position: absolute; left: 120px; top: 120px;
    width: 100px; height: 100px; border-radius: 50%;
    background: var(--teal-dark);
  }
  .divider {
    position: absolute; left: 268px; top: 78px;
    width: 2px; height: 150px; background: var(--teal-dark);
  }
  .details { position: absolute; left: 298px; top: 46px; color: var(--ink); }
  .person-name {
    font-family: "Raleway", Arial, sans-serif; font-weight: 800;
    font-size: 30px; letter-spacing: -0.3px; line-height: 1;
  }
  .person-role { font-size: 15px; color: var(--ink-soft); margin-top: 4px; }
  .address { font-size: 15px; line-height: 1.3; margin-top: 12px; letter-spacing: 0.3px; }
  .contact-list { list-style: none; margin-top: 10px; font-size: 15px; line-height: 1.35; letter-spacing: 0.3px; }
  .contact-list li { display: flex; align-items: center; gap: 8px; }
  .contact-list svg { width: 11px; height: 11px; flex: none; }
</style>
</head>
<body>
  <section class="card card-back" aria-label="Card back">
    <div class="brand">
      <span class="brand-dot"></span>
      <span class="brand-name">BrightNestly</span>
    </div>
    <p class="back-url">www.brightnestly.com</p>
  </section>

  <section class="card card-front" aria-label="Card front">
    <svg class="front-wave" viewBox="0 0 640 366" aria-hidden="true">
      <path d="M0 366 L0 352 C140 345 240 335 330 305 C420 275 470 268 530 280 C580 290 610 300 640 302 L640 366 Z" fill="#477077"/>
      <path d="M0 352 C140 345 240 335 330 305 C420 275 470 268 530 280 C580 290 610 300 640 302" fill="none" stroke="#ffffff" stroke-width="3"/>
      <path d="M0 347 C140 340 240 330 328 300 C418 270 470 262 530 274 C580 284 610 294 640 296" fill="none" stroke="#6ba8b2" stroke-width="3"/>
    </svg>
    <span class="front-mark"></span>
    <span class="divider"></span>
    <div class="details">
      <h1 class="person-name">Lena Hartwell</h1>
      <p class="person-role">Founder</p>
      <p class="address">48 Kowhai Terrace, Ferndale<br>Auckland 1071, New Zealand</p>
      <ul class="contact-list">
        <li><svg viewBox="0 0 12 12"><rect x="3" y="1" width="6" height="10" rx="1" fill="none" stroke="#477077" stroke-width="1.4"/></svg>021 437 518</li>
        <li><svg viewBox="0 0 12 12"><path d="M2 2 Q2 9 10 10 L10 8 L8 7 L7 8 Q4 7 4 5 L5 4 L4 2 Z" fill="#477077"/></svg>+64 (0)9 581 4706</li>
        <li><svg viewBox="0 0 12 12"><circle cx="6" cy="6" r="5" fill="none" stroke="#477077" stroke-width="1.3"/><path d="M1 6 H11 M6 1 Q3 6 6 11 Q9 6 6 1" fill="none" stroke="#477077" stroke-width="1"/></svg>www.brightnestly.com</li>
      </ul>
    </div>
  </section>
</body>
</html>
```